New Business Card for General Contractor Marketing

Need a business card the is more like a marketing promotion of our services
Must be horizontal orientation, One Sided Only, Max font size, Organize the Services
#1 General Contractor for Realtors
Remodels – Renovations – Repairs
Water & Mold Damage Experts
Painting: Interior/ Exterior
Flooring: Wood / LVT / Carpet
Plumbing: Repairs & Upgrades
Electric: Lights & Energy Efficient Upgrades
Kitchen & Bath Remodels
Fast Inspections Repair Billed Thru Escrow
BrightHarborBuilds.com
555-418-2796

Industry/Entity Type

General Contractor

Contact Information for Business Card

One Sided Only: #1 General Contractor for Realtors Remodels – Renovations – Repairs Water & Mold Damage Experts Painting: Interior/ Exterior Flooring: Wood / LVT / Carpet Plumbing: Repairs & Upgrades Electric: Lights & Energy Efficient Upgrades Kitchen & Bath Remodels Fast Inspections Repair Billed Thru Escrow BrightHarborBuilds.com 555-418-2796

Colors
0054AA
0677BA
7BADD7
CADEEF
E8F1F8

Requirements
Must have
• One Sided Only: #1 General Contractor for Realtors Remodels – Renovations – Repairs Water & Mold Damage Experts Painting: Interior/ Exterior Flooring: Wood / LVT / Carpet Plumbing: Repairs & Upgrades Electric: Lights & Energy Efficient Upgrades Kitchen & Bath Remodels Fast Inspections Repair Billed Thru Escrow BrightHarborBuilds.com 555-418-2796

```html
<!DOCTYPE html>
<html lang="en">
<head>
<meta charset="UTF-8">
<title>Bright Harbor Builds – Business Card</title>
<link href="https://fonts.googleapis.com/css2?family=Montserrat:wght@500;600;700;800&display=swap" rel="stylesheet">
<style>
  :root{
    --navy:#0b1f5c;
    --blue-deep:#0a2b8c;
    --blue-bright:#1766e8;
    --orange:#ff7a00;
    --white:#ffffff;
    --stage:#e8ecf2;
  }
  *{margin:0;padding:0;box-sizing:border-box}
  html,body{width:1200px;height:800px;overflow:hidden;background:var(--stage);font-family:'Montserrat',sans-serif}
  .card{
    position:absolute;left:100px;top:114px;width:1000px;height:572px;
    background:var(--white);border-radius:16px;overflow:hidden;
    box-shadow:0 10px 30px rgba(10,30,80,.18);
  }
  .accent-tab{position:absolute;left:0;top:20px;width:40px;height:110px;background:var(--orange);border-radius:0 10px 10px 0}
  .brand{
    position:absolute;left:66px;top:46px;width:290px;display:flex;align-items:center;gap:12px;
  }
  .brand-mark{flex:0 0 28px;width:28px;height:28px;background:var(--orange)}
  .brand-name{font-weight:800;font-size:24px;line-height:1.15;color:var(--navy);letter-spacing:.3px;white-space:nowrap}
  .contact-bar{
    position:absolute;left:372px;top:20px;right:0;height:106px;background:var(--navy);
    border-radius:14px 0 0 14px;display:flex;align-items:center;justify-content:center;gap:28px;
    color:var(--white);font-weight:600;font-size:25px;
  }
  .contact-item{display:flex;align-items:center;gap:12px;white-space:nowrap}
  .contact-item svg{width:32px;height:32px}
  .services{
    position:absolute;left:0;top:221px;right:0;bottom:0;
    background:linear-gradient(110deg,var(--blue-deep) 0%,#0f47c4 55%,var(--blue-bright) 100%);
    border-top:7px solid var(--orange);
    padding:48px 32px 0 30px;color:var(--white);
  }
  .headline{font-weight:800;font-size:27.5px;line-height:40px;text-transform:uppercase}
  .service-list{margin-top:22px;font-weight:500;font-size:27px;line-height:36px;text-align:justify;text-align-last:left}
  .service-list strong{font-weight:700}
  .emergency-badge{
    position:absolute;left:684px;top:181px;width:282px;height:66px;background:var(--orange);
    border-radius:33px;border:4px solid var(--white);
    display:flex;align-items:center;justify-content:center;gap:6px;color:var(--white);
    box-shadow:0 3px 8px rgba(0,0,0,.2);
  }
  .badge-hours{font-weight:800;font-size:50px;line-height:1}
  .badge-text{display:flex;flex-direction:column;line-height:1}
  .badge-small{font-weight:700;font-size:13px;letter-spacing:.5px}
  .badge-large{font-weight:800;font-size:34px}
</style>
</head>
<body>
  <div class="card">
    <div class="accent-tab"></div>
    <div class="brand">
      <span class="brand-mark"></span>
      <span class="brand-name">BRIGHT HARBOR<br>BUILDS</span>
    </div>
    <div class="contact-bar">
      <span class="contact-item">
        <svg viewBox="0 0 32 32" aria-hidden="true"><circle cx="16" cy="16" r="15" fill="#ff7a00"/><path d="M11 9c1-1 2.5-.6 3 .6l1 2.4c.3.8 0 1.6-.6 2l-1 .8c.8 1.8 2.2 3.2 4 4l.8-1c.5-.6 1.3-.8 2-.5l2.4 1c1.2.5 1.6 2 .6 3-1.4 1.4-3.4 1.9-5.4 1.1-3.8-1.6-6.8-4.6-8.4-8.4-.8-2-.3-4 1.100-5.4z" fill="#fff"/></svg>
        555-418-2796
      </span>
      <span class="contact-item">
        <svg viewBox="0 0 32 32" aria-hidden="true"><circle cx="16" cy="16" r="15" fill="#ff7a00"/><g fill="none" stroke="#fff" stroke-width="2"><circle cx="16" cy="16" r="9"/><ellipse cx="16" cy="16" rx="4" ry="9"/><path d="M7 16h18M8.5 11.5h15M8.5 20.5h15"/></g></svg>
        brightharborbuilds.com
      </span>
    </div>
    <section class="services">
      <h1 class="headline">#1 General Contractor for Realtors Remodels<br>– Renovations – Repairs Water &amp; Mold Damage</h1>
      <p class="service-list">Experts <strong>Painting:</strong> Interior/ Exterior <strong>Flooring:</strong> Wood / LVT / Carpet <strong>Plumbing:</strong> Repairs &amp; Upgrades <strong>Electric:</strong> Lights &amp; Energy Efficient Upgrades Kitchen &amp; Bath Remodels Fast Inspections Repair Billed Thru Escrow</p>
    </section>
    <div class="emergency-badge">
      <span class="badge-hours">24</span>
      <span class="badge-text"><span class="badge-small">HOUR EMERGENCY</span><span class="badge-large">SERVICE</span></span>
    </div>
  </div>
</body>
</html>
```